Hi, Looking for an upgraded business card to the aged one attached. Open to suggestions and no real limitations, but if your going to use a picture of a taxi i think it should be vector based rather than a full color picture. I've uploaded a 2 pictures of the type of taxi which is a Velmora K7 in white. The taxi markings look like the pink one in the picture but to be clear his is white. The taxi is in Bermuda so if you wanted to include something island based that's ok as well but not required. The other thing he wanted to keep on there was the bermuda police crest, with the retired police office incorporated somehow.

Requirements
Must have
• Bermuda Taxi Operator
Retired Police Officer
Police Crest
Taxi #
Email
Mobile Number

```html
<!DOCTYPE html>
<html lang="en">
<head>
<meta charset="utf-8">
<title>Bermuda Taxi Operator – Business Card</title>
<link href="https://fonts.googleapis.com/css2?family=Roboto:wght@300;400;500&display=swap" rel="stylesheet">
<style>
  :root {
    --stage: #454545;
    --paper: #ffffff;
    --navy: #1f5a9c;
    --sky: #5c9dd8;
    --accent: #2f6197;
    --illustration-light: #eef3f9;
    --illustration-dark: #c9d8ea;
  }
  * { margin: 0; padding: 0; box-sizing: border-box; }
  html, body {
    width: 1200px; height: 876px; overflow: hidden;
    background: var(--stage);
    font-family: "Roboto", Arial, sans-serif;
  }
  .canvas {
    width: 1200px; height: 876px;
    display: flex; flex-direction: column; align-items: center; justify-content: center;
    gap: 26px;
  }
  .card {
    position: relative;
    width: 700px; height: 400px;
    background: var(--paper);
    overflow: hidden;
    box-shadow: 0 10px 28px rgba(0,0,0,.35);
  }

  /* Front */
  .card-front .service-title {
    position: absolute; left: 60px; top: 34px;
    font-weight: 500; font-size: 28px; letter-spacing: .5px;
    color: var(--navy); text-transform: uppercase;
  }
  .card-front .operator-name {
    position: absolute; left: 60px; top: 118px;
    font-weight: 500; font-size: 28px; color: var(--navy);
  }
  .card-front .operator-role {
    position: absolute; left: 60px; top: 154px;
    font-weight: 300; font-size: 19px; color: var(--navy);
  }
  .card-front .divider {
    position: absolute; left: 60px; top: 196px;
    width: 360px; height: 2px; background: var(--navy);
  }
  .contact-list {
    position: absolute; left: 44px; top: 216px;
    list-style: none;
  }
  .contact-list li {
    display: flex; align-items: center; gap: 12px;
    font-weight: 300; font-size: 19px; color: var(--navy);
    margin-bottom: 12px;
  }
  .contact-list svg { width: 16px; height: 16px; flex: none; }
  .taxi-number {
    position: absolute; left: 300px; top: 318px;
    font-weight: 300; font-size: 22px; color: var(--navy);
  }
  .front-band {
    position: absolute; left: 0; bottom: 0; width: 700px; height: 18px;
  }

  /* Emblem stand-in */
  .emblem {
    position: absolute;
    display: flex; align-items: center; justify-content: center; gap: 12px;
    color: var(--navy); font-weight: 500; font-size: 26px;
    text-align: center; line-height: 1.15;
    width: 220px; height: 170px;
  }
  .emblem-dot {
    width: 18px; height: 18px; border-radius: 50%; background: var(--navy); flex: none;
  }
  .card-front .emblem { left: 450px; top: 110px; }
  .card-back .emblem  { left: 450px; top: 205px; }

  /* Back */
  .back-art { position: absolute; inset: 0; width: 700px; height: 400px; }
</style>
</head>
<body>
<main class="canvas">

  <section class="card card-front" aria-label="Card front">
    <h1 class="service-title">Bermuda Taxi Operator</h1>

    <div class="emblem" aria-label="Harbour Watch Guild">
      <span class="emblem-dot"></span>
      <span>Harbour<br>Watch Guild</span>
    </div>

    <p class="operator-name">Desmond Whitaker</p>
    <p class="operator-role">Retired Police Officer</p>
    <div class="divider"></div>

    <ul class="contact-list">
      <li>
        <svg viewBox="0 0 16 16" aria-hidden="true"><path d="M4 1.5 6 4.5 4.8 6c.8 2 2.3 3.5 4.2 4.3L10.5 9l3 2-1.2 2.6C7 13.4 2.6 9 2.4 3.1Z" fill="none" stroke="#1f5a9c" stroke-width="1.4" stroke-linejoin="round"/></svg>
        1-441-555-0142
      </li>
      <li>
        <svg viewBox="0 0 16 16" aria-hidden="true"><rect x="1.5" y="3.5" width="13" height="9" fill="none" stroke="#1f5a9c" stroke-width="1.4"/><path d="M1.5 3.5 8 9l6.5-5.5" fill="none" stroke="#1f5a9c" stroke-width="1.4"/></svg>
        dwhitaker27@mailbox.com
      </li>
    </ul>

    <p class="taxi-number">Taxi #T2481</p>

    <svg class="front-band" viewBox="0 0 700 18" preserveAspectRatio="none" aria-hidden="true">
      <rect x="0" y="0" width="700" height="18" fill="var(--sky)"/>
      <polygon points="0,0 520,0 505,18 0,18" fill="var(--navy)"/>
    </svg>
  </section>

  <section class="card card-back" aria-label="Card back">
    <svg class="back-art" viewBox="0 0 700 400">
      <defs>
        <linearGradient id="taxiArea" x1="0" y1="0" x2="0.5" y2="1">
          <stop offset="0" stop-color="var(--illustration-light)"/>
          <stop offset="1" stop-color="var(--illustration-dark)"/>
        </linearGradient>
      </defs>
      <polygon points="0,0 588,0 322,400 0,400" fill="url(#taxiArea)" role="img" aria-label="Vector illustration of a white taxi van on a Bermuda street"/>
      <polygon points="360,0 588,0 455,200" fill="var(--accent)" aria-hidden="true"/>
    </svg>

    <div class="emblem" aria-label="Harbour Watch Guild">
      <span class="emblem-dot"></span>
      <span>Harbour<br>Watch Guild</span>
    </div>
  </section>

</main>
</body>
</html>
```